Trade Show Norvane 3x3 booth schel scheme

We would like to have full coverage design for 3x3 booth scheel

2x2 pop up Counter (1200mm wide x 900mm high x 400mm deep)
Our company provides food safety training, consultancy and food safety app service for hospitality businesses.

```html
<!DOCTYPE html>
<html lang="en">
<head>
<meta charset="utf-8">
<title>Norvane Booth Graphics</title>
<link rel="stylesheet" href="https://fonts.googleapis.com/css2?family=Archivo+Black&family=Montserrat:wght@500&display=swap">
<style>
  :root {
    --backdrop: #8aabd6;
    --lime: #cdd631;
    --lime-deep: #6c9a12;
    --cream: #fdfde2;
    --charcoal: #2b2b2b;
    --ink: #0d0d0d;
    --white: #ffffff;
    --badge: #2fb52a;
    --dot-orange: #f7a13a;
  }
  * { margin: 0; padding: 0; box-sizing: border-box; }
  html, body { width: 1200px; height: 905px; overflow: hidden; background: var(--backdrop); }
  .stage { position: relative; width: 1200px; height: 905px; }

  .panel { position: absolute; overflow: hidden; }
  .headline { font-family: "Archivo Black", sans-serif; text-transform: uppercase; white-space: nowrap; position: absolute; line-height: 1; }
  .wordmark { font-family: "Montserrat", sans-serif; font-weight: 500; position: absolute; white-space: nowrap; line-height: 1; }

  /* Panel: promise */
  .promise { left: 53px; top: 52px; width: 537px; height: 443px; background: var(--cream); }
  .promise .lime-field { position: absolute; left: 194px; top: 0; width: 323px; height: 443px; background: var(--lime); }
  .promise .portrait { position: absolute; left: 35px; top: 35px; width: 175px; height: 408px; border-radius: 80px 80px 0 0; background: linear-gradient(180deg, #7a5540 0%, #c7a68a 35%, #d9c2a8 60%, #2a2320 100%); }
  .promise .wordmark { left: 212px; top: 50px; font-size: 36px; letter-spacing: 11px; color: var(--ink); }
  .promise .promise-band { position: absolute; left: 194px; top: 161px; width: 304px; height: 61px; background: var(--lime-deep); }
  .promise .promise-band .headline { left: 18px; top: 16px; font-size: 26px; letter-spacing: -1.4px; color: var(--white); }
  .promise .peace { left: 213px; top: 226px; font-size: 77px; letter-spacing: -5px; color: var(--charcoal); }
  .promise .of-tag { position: absolute; left: 212px; top: 306px; width: 52px; height: 30px; background: var(--lime-deep); }
  .promise .of-tag .headline { left: 5px; top: 5px; font-size: 22px; letter-spacing: -1.5px; color: var(--white); }
  .promise .mind { left: 268px; top: 285px; font-size: 77px; letter-spacing: -5px; color: var(--charcoal); }
  .promise .bang { left: 452px; top: 272px; font-size: 104px; color: var(--lime-deep); transform: rotate(8deg); }
  .badge { position: absolute; }

  /* Panel: rating */
  .rating { left: 611px; top: 52px; width: 537px; height: 443px; background: var(--cream); }
  .rating .lime-sweep { position: absolute; inset: 0; }
  .rating .kicker { left: 53px; top: 60px; font-size: 25px; letter-spacing: -1.3px; color: var(--ink); }
  .rating .big { left: 51px; font-size: 69px; letter-spacing: -3px; color: var(--ink); }
  .rating .big.l1 { top: 93px; }
  .rating .big.l2 { top: 150px; }
  .rating .big.l3 { top: 207px; }
  .rating .experts-box { position: absolute; left: 32px; top: 276px; width: 366px; height: 90px; background: var(--ink); }
  .rating .experts-box .headline { left: 19px; font-size: 37px; letter-spacing: -2.2px; color: var(--white); }
  .rating .experts-box .e1 { top: 10px; }
  .rating .experts-box .e2 { top: 45px; }
  .rating .review-bubble { position: absolute; left: 340px; top: 83px; width: 173px; height: 108px; border-radius: 34px; transform: rotate(8deg); background: linear-gradient(160deg, #ffffff 0%, #ecebe4 70%, #d9d8cf 100%); }
  .rating .wordmark { left: 374px; top: 398px; font-size: 22px; letter-spacing: 7px; color: var(--ink); }

  /* Panel: banner */
  .banner { left: 256px; top: 540px; width: 688px; height: 301px; background: var(--charcoal); }
  .banner .leaves { position: absolute; left: 190px; top: 0; width: 117px; height: 65px; border-radius: 0 0 58px 58px; background: linear-gradient(90deg, #8fb52a 0%, #b9cf3a 100%); }
  .banner .wordmark { left: 0; width: 100%; text-align: center; top: 112px; font-size: 50px; letter-spacing: 15px; padding-left: 15px; color: var(--white); }
  .banner .service-line { left: 0; width: 100%; text-align: center; font-size: 36px; letter-spacing: -2px; color: var(--white); }
  .banner .service-line.s1 { top: 183px; }
  .banner .service-line.s2 { top: 225px; }
  .banner .accent { color: var(--lime); }
  .banner .dots { position: absolute; inset: 0; }
</style>
</head>
<body>
<main class="stage">

  <section class="panel promise">
    <div class="lime-field"></div>
    <div class="portrait" role="img" aria-label="Photo of a smiling businesswoman in a beige blazer reading a tablet"></div>
    <svg class="badge" style="left:18px;top:134px" width="58" height="58" viewBox="0 0 58 58" aria-hidden="true">
      <circle cx="29" cy="29" r="28" fill="var(--badge)"/>
      <path d="M17 30 L26 38 L42 21" fill="none" stroke="#fff" stroke-width="6" stroke-linecap="round" stroke-linejoin="round"/>
    </svg>
    <svg class="badge" style="left:453px;top:92px" width="76" height="76" viewBox="0 0 76 76" aria-hidden="true">
      <circle cx="38" cy="38" r="37" fill="var(--badge)"/>
      <path d="M22 40 L34 50 L55 27" fill="none" stroke="#fff" stroke-width="8" stroke-linecap="round" stroke-linejoin="round"/>
    </svg>
    <div class="wordmark">NORVANE</div>
    <div class="promise-band"><span class="headline">Our promise is</span></div>
    <div class="headline peace">Peace</div>
    <div class="of-tag"><span class="headline">of</span></div>
    <div class="headline mind">Mind</div>
    <div class="headline bang">!</div>
  </section>

  <section class="panel rating">
    <svg class="lime-sweep" width="537" height="443" viewBox="0 0 537 443" aria-hidden="true">
      <path d="M0 0 H537 V208 C470 330 330 440 200 432 C110 428 40 400 0 380 Z" fill="var(--lime)"/>
    </svg>
    <div class="headline kicker">Achieve &amp; maintain</div>
    <div class="headline big l1">5 Star</div>
    <div class="headline big l2">Hygiene</div>
    <div class="headline big l3">Rating</div>
    <div class="review-bubble" role="img" aria-label="3D speech bubble showing a five gold star review"></div>
    <div class="experts-box">
      <span class="headline e1">With experts</span>
      <span class="headline e2">at your side!</span>
    </div>
    <div class="wordmark">NORVANE</div>
  </section>

  <section class="panel banner">
    <div class="leaves" role="img" aria-label="Two illustrated green leaves"></div>
    <svg class="dots" width="688" height="301" viewBox="0 0 688 301" aria-hidden="true">
      <circle cx="463" cy="53" r="6" fill="var(--lime)"/>
      <circle cx="502" cy="49" r="6" fill="var(--lime)"/>
      <circle cx="509" cy="81" r="6" fill="var(--lime)"/>
      <circle cx="493" cy="278" r="6" fill="var(--dot-orange)"/>
      <circle cx="483" cy="296" r="3" fill="var(--lime)"/>
    </svg>
    <div class="wordmark">NORVANE</div>
    <div class="headline service-line s1">Food <span class="accent">Hygiene</span></div>
    <div class="headline service-line s2"><span class="accent">Health</span> Safety</div>
  </section>

</main>
</body>
</html>
```